Bluestone Advisory & Mgmt - Professional Business Cards

Hi!

I am a Real Estate Developer and Construction Consultant.

I have a lot of inspiration from previous designs and would be open to using the attached Designs as a starting point. I would like to see these styles incorporated into your designs.

I really need professional business card to go with it that includes my important info.

Look forward to seeing your designs!.

Target Market(s)

My Target market are building owners, lawyers, consultants.

Industry/Entity Type

Real Estate Development

Contact Information for Business Card

My Name: Dorian Pelkey
My Title: Principle
Company Name: Bluestone Advisory & Mgmt, LLC
Address: 348 West 71st Street, 9th FL New York, NY 10010
Mobile: 917.806.3971
Website: bam-hvx.example

Font styles to use
Serif
Sans Serif

Colors

Designer to choose colors to be used in the design.

Requirements
Must have
• Must incorporate the logo attached or have new that looks similar.
• Must use professional font that will be seen and judged by wealthy land owners and developers.
• Must incorporate some of the color green.
Should not have
• Photo's or pictures of people or buildings of any kind.

```html
<!DOCTYPE html>
<html lang="en">
<head>
<meta charset="utf-8">
<title>Bluestone Advisory &amp; Mgmt - Business Cards</title>
<link rel="stylesheet" href="https://fonts.googleapis.com/css2?family=Raleway:wght@600&family=Arimo:wght@700&family=Open+Sans:wght@400&display=swap">
<style>
  :root {
    --green: #4fb779;
    --grey: #9a9292;
    --grey-dark: #8a8282;
    --white: #ffffff;
    --backdrop: #e6e6e6;
  }
  * { margin: 0; padding: 0; box-sizing: border-box; }
  html, body {
    width: 1125px; height: 1200px; overflow: hidden;
    background: var(--backdrop);
  }
  .card {
    position: absolute;
    border-radius: 26px;
    overflow: hidden;
  }
  .card--front { left: 137px; top: 95px; width: 849px; height: 481px; background: var(--white); }
  .card--back { left: 146px; top: 624px; width: 841px; height: 499px; background: var(--green); }

  .brand {
    position: absolute;
    font-family: "Raleway", sans-serif;
    font-weight: 600;
    line-height: 1;
  }
  .card--front .brand { left: 92px; top: 112px; color: var(--green); }
  .brand__name { display: block; font-size: 68px; letter-spacing: -1px; }
  .card--front .brand__sub { display: block; font-size: 33px; margin-top: 18px; }
  .card--back .brand { left: 214px; top: 90px; color: var(--white); }
  .card--back .brand__name { font-size: 92px; letter-spacing: -1px; }
  .card--back .brand__sub { display: block; font-size: 44px; margin-top: 24px; }

  .divider {
    position: absolute; left: 463px; top: 106px;
    width: 2px; height: 189px; background: #d6d2d2;
  }
  .person { position: absolute; left: 500px; top: 110px; }
  .person__name {
    font-family: "Arimo", sans-serif; font-weight: 700;
    font-size: 27px; color: var(--green); letter-spacing: 0.3px;
  }
  .person__title {
    font-family: "Arimo", sans-serif; font-weight: 700;
    font-size: 24px; color: var(--grey-dark); margin-top: 4px;
  }
  .contacts { list-style: none; margin-top: 20px; }
  .contacts li {
    display: flex; align-items: center; gap: 12px;
    font-family: "Open Sans", sans-serif; font-size: 20px;
    color: var(--grey-dark); height: 36px;
  }
  .contacts svg { width: 18px; height: 18px; flex: none; }
  .contacts .web { letter-spacing: 1.5px; }

  .wave { position: absolute; left: 0; top: 0; width: 849px; height: 481px; }
  .address {
    position: absolute; left: 72px; top: 404px;
    font-family: "Open Sans", sans-serif; font-size: 19px;
    line-height: 31px; color: var(--white);
  }

  .back-web {
    position: absolute; left: 0; right: 0; top: 372px;
    text-align: center;
    font-family: "Open Sans", sans-serif; font-size: 26px;
    letter-spacing: 4px; color: var(--white);
  }
</style>
</head>
<body>
  <section class="card card--front">
    <svg class="wave" viewBox="0 0 849 481" aria-hidden="true">
      <path d="M0,392 C170,345 400,368 600,432 C710,466 790,452 849,430 L849,481 L0,481 Z" fill="var(--green)"/>
      <path d="M0,382 C190,330 430,356 630,420 C730,452 800,440 849,418" fill="none" stroke="var(--grey)" stroke-width="2.5"/>
      <path d="M440,400 C560,430 650,455 730,452 C790,450 825,440 849,432" fill="none" stroke="var(--white)" stroke-width="4"/>
    </svg>

    <div class="brand">
      <span class="brand__name">Bluestone</span>
      <span class="brand__sub">Advisory &amp; Mgmt</span>
    </div>

    <div class="divider"></div>

    <div class="person">
      <p class="person__name">DORIAN PELKEY</p>
      <p class="person__title">Principle</p>
      <ul class="contacts">
        <li>
          <svg viewBox="0 0 20 20"><circle cx="10" cy="10" r="8.5" fill="none" stroke="var(--green)" stroke-width="2"/><path d="M7,5.5 l2,0 l0.6,2.6 l-1.3,1 a6,6 0 0 0 2.6,2.6 l1-1.3 l2.6,0.6 l0,2 a7,7 0 0 1 -7.5,-7.5z" fill="var(--green)"/></svg>
          <span>917.806.3971</span>
        </li>
        <li>
          <svg viewBox="0 0 20 20"><path d="M2,8 L10,3 L18,8 L18,17 L2,17 Z" fill="var(--green)"/><path d="M2,8 L10,13 L18,8" fill="none" stroke="var(--white)" stroke-width="1.5"/></svg>
          <span>office@bam-hvx.example</span>
        </li>
        <li>
          <svg viewBox="0 0 20 20" fill="none" stroke="var(--green)" stroke-width="1.5"><circle cx="10" cy="10" r="8"/><ellipse cx="10" cy="10" rx="3.5" ry="8"/><path d="M2,10 H18 M3.5,6 H16.5 M3.5,14 H16.5"/></svg>
          <span class="web">www.bam-hvx.example</span>
        </li>
      </ul>
    </div>

    <p class="address">348 West 71st Street,<br>9th FL New York, NY 10010</p>
  </section>

  <section class="card card--back">
    <div class="brand">
      <span class="brand__name">Bluestone</span>
      <span class="brand__sub">Advisory &amp; Mgmt</span>
    </div>
    <p class="back-web">www.bam-hvx.example</p>
  </section>
</body>
</html>
```